Intelligent design image for our website

I would like an awesome image for our website that showcases the intelligent design of our app. We currently have a test web site here.
https://www.roadpine.com.au/test-ewd/
I really do not like the graphic next to the "Intelligent design" and i want something much better than this.
Our app is used by Australian Truck Drivers. It would be nice to have a little bit of an Australian feel, but most importantly is should clearly showcase our app look a feel and the screens should be as legible (readable) as possible. These examples could be used for inspiration.
https://pixelmarigold.net/products/free-app-showcase-mockup-psd-3903046
https://www.vantrel.com/community/file/1118736476036244148/MobileApp-Landing-Page-Template-for-Mobile-Apps-Showcase

```html
<!DOCTYPE html>
<html lang="en">
<head>
<meta charset="utf-8">
<title>Work and Rest Dashboard</title>
<link href="https://fonts.googleapis.com/css2?family=Lato:wght@400;700;900&display=swap" rel="stylesheet">
<style>
:root{
  --bg:#ffffff;
  --ink:#1d1f24;
  --muted:#6b6f78;
  --blue:#5b93d8;
  --blue-dark:#3a6fe6;
  --blue-soft:#a9bff5;
  --halo:#d7e9f8;
  --line:#e3e6ec;
  --red:#e0584f;
}
*{box-sizing:border-box;margin:0;padding:0}
html,body{width:1200px;height:1155px;overflow:hidden;background:var(--bg);font-family:'Lato',sans-serif;color:var(--ink)}
.canvas{position:relative;width:1200px;height:1155px}
.links{position:absolute;inset:0;pointer-events:none}

/* callouts */
.callout{position:absolute;width:340px;height:125px;text-align:center;display:flex;flex-direction:column;justify-content:center}
.callout::before{content:"";position:absolute;inset:12px -12px -12px 12px;background:var(--halo);border-radius:10px;z-index:0}
.callout::after{content:"";position:absolute;inset:0;background:#fff;border:2px solid var(--blue);border-radius:10px;z-index:1}
.callout span{position:relative;z-index:2}
.callout .time{font-size:36px;font-weight:700;letter-spacing:.5px}
.callout .label{font-size:27px;color:var(--muted);line-height:1.2}
.callout.tall{height:148px}

/* cards */
.card{position:absolute;background:#fff;border-radius:12px;box-shadow:0 8px 28px rgba(40,60,100,.13);border-top:3px solid var(--blue);font-size:9px}
.tab{position:absolute;top:-3px;left:50%;transform:translateX(-50%);background:var(--blue);color:#fff;font-size:11px;padding:5px 26px 6px;white-space:nowrap;clip-path:polygon(0 0,100% 0,88% 100%,12% 100%)}
.info{position:absolute;top:7px;right:9px;width:15px;height:15px;border:1.5px solid var(--blue);border-radius:50%;color:var(--blue);font-size:9px;font-weight:700;text-align:center;line-height:12px}
.pair{display:flex;justify-content:space-around;text-align:center}
.val{font-size:11px;font-weight:700}
.cap{font-size:8.5px;color:var(--muted)}
.grid{display:grid;grid-template-columns:1fr 1fr;text-align:center}
.grid>div{position:relative;padding:6px 0;border-bottom:1px solid var(--line)}
.grid>div:nth-child(odd){border-right:1px solid var(--line)}
.grid>div:nth-last-child(-n+2){border-bottom:none}
.bar{height:8px;border-radius:4px;background:var(--blue-soft);overflow:hidden}
.bar i{display:block;height:100%;background:var(--blue-dark)}
.pager{display:flex;justify-content:space-between;align-items:center;text-align:center}
.btn{border:1px solid var(--blue-soft);color:var(--blue-soft);border-radius:3px;padding:3px 12px;font-size:9px}
.dot{position:absolute;width:10px;height:10px;border-radius:50%;background:var(--blue)}
.cell-dot{position:absolute;right:2px;top:50%;margin-top:-5px;width:10px;height:10px;border-radius:50%;background:var(--blue)}

/* day circles */
.days{display:flex;flex-wrap:wrap;gap:6px}
.day{width:20px;height:20px;border-radius:50%;border:1.5px solid var(--blue);color:var(--blue);font-size:8px;display:flex;align-items:center;justify-content:center}
.day.miss{border-color:var(--red);color:var(--red);background:linear-gradient(135deg,transparent 45%,var(--red) 46%,var(--red) 54%,transparent 55%)}
.day.now{background:var(--blue);color:#fff}

/* phone screen */
.screen{position:absolute;left:667px;top:412px;width:318px;height:676px;background:#fff;border-radius:38px;box-shadow:0 10px 40px rgba(40,60,100,.18);overflow:hidden;font-size:10px}
.status{display:flex;justify-content:space-between;padding:14px 24px 0;font-weight:700;font-size:12px}
.head{display:flex;justify-content:space-between;align-items:flex-end;padding:14px 16px 10px;border-bottom:1px solid var(--line)}
.head .name{font-size:12px}
.head .lic{font-size:11px;color:var(--muted);margin-top:8px}
.sync{background:var(--blue);color:#fff;font-size:9px;padding:3px 7px;border-radius:2px}
.option{padding:12px 16px 0}
.select{display:flex;justify-content:space-between;font-size:12px;padding:12px 0 8px;border-bottom:1px solid var(--line)}
.screen .card{position:relative;margin:12px 16px 0;box-shadow:0 3px 10px rgba(40,60,100,.12);border-radius:6px}
.nav{position:absolute;bottom:0;left:0;right:0;height:78px;background:#fff;border-top:1px solid var(--line);display:flex;justify-content:space-around;padding-top:12px;font-size:9.5px;text-align:center}
.nav b{display:block;font-size:15px;font-weight:400;margin-bottom:4px}

/* calendar card */
.chart{position:relative;height:90px;background:linear-gradient(#fff,#f3f5f8);border-radius:12px 12px 0 0;border-bottom:1px solid var(--line)}
.chart i{position:absolute;bottom:18px;width:8px;border-radius:4px;background:var(--blue-soft)}
.chip{display:inline-block;border:1.5px solid var(--blue);color:var(--blue);border-radius:4px;padding:2px 8px;font-size:10px;font-weight:700}
</style>
</head>
<body>
<div class="canvas">

<svg class="links" width="1200" height="1155" viewBox="0 0 1200 1155">
  <g stroke="#5b93d8" stroke-width="2" fill="none">
    <line x1="710" y1="150" x2="627" y2="305"/>
    <line x1="1040" y1="350" x2="954" y2="833"/>
    <line x1="197" y1="545" x2="197" y2="813"/>
  </g>
</svg>

<!-- daily summary card -->
<div class="card summary" style="left:18px;top:165px;width:262px;height:240px;border-top:none">
  <div class="chart">
    <i style="left:30px;height:36px"></i><i style="left:56px;height:50px"></i><i style="left:82px;height:30px;background:var(--blue-dark)"></i>
    <span class="cap" style="position:absolute;bottom:4px;left:24px">22 &nbsp;&nbsp;&nbsp;&nbsp; 23 &nbsp;&nbsp;&nbsp;&nbsp; 24 &nbsp;&nbsp;&nbsp;&nbsp; 25</span>
  </div>
  <div style="padding:10px 14px">
    <span class="chip">Fri 25 Aug 2023</span>
    <div class="grid" style="margin-top:8px">
      <div><div class="val">07:03</div><div class="cap">Total Work</div></div>
      <div><div class="val">03:46</div><div class="cap">Total Rest</div></div>
      <div><div class="val">03:14</div><div class="cap">Night Work</div></div>
      <div><div class="val">04:46</div><div class="cap">Max Night Rest</div></div>
      <div><div class="val">00:00</div><div class="cap">Long Work</div></div>
      <div><div class="val" style="color:var(--red)">✕</div><div class="cap">Night Rest Break</div></div>
    </div>
  </div>
</div>

<!-- 14 day rule card -->
<div class="card" style="left:300px;top:180px;width:335px;height:300px">
  <div class="tab">14 day Rule</div><div class="info">i</div>
  <div class="pair" style="margin-top:30px">
    <div><div class="val">01:17 14-Aug</div><div class="cap">Period Start</div></div>
    <div><div class="val">01:17 28-Aug</div><div class="cap">Period End</div></div>
  </div>
  <div style="padding:10px 12px 0">
    <div class="cap" style="margin-bottom:4px">Work Completed</div>
    <div class="bar"><i style="width:54%"></i></div>
    <div class="pager cap" style="margin-top:3px"><span>0 hr</span><span>144 hr</span></div>
    <div class="grid" style="margin-top:6px">
      <div><div class="val">78:08</div><div class="cap">Work Completed</div></div>
      <div><div class="val">43:01</div><div class="cap">Maximum Continuous Rest</div></div>
      <div><div class="val">65:52</div><div class="cap">Work Remaining</div></div>
      <div><div class="val">01:17 27-Aug</div><div class="cap">Start 24 hr Rest Before</div></div>
      <div><div class="val">62:29</div><div class="cap">Period Remaining</div></div>
      <div><div class="val">1 / 2</div><div class="cap">24 hr Rests Found/Required</div></div>
    </div>
    <div class="pager" style="margin-top:8px"><span class="btn">‹ Previous</span><span><span class="val">1/4</span><br><span class="cap">Active Periods</span></span><span class="btn">Next ›</span></div>
  </div>
  <div class="dot" style="left:322px;top:120px"></div>
</div>

<!-- night rests card -->
<div class="card" style="left:185px;top:470px;width:300px;height:175px">
  <div class="tab">Night Rests</div><div class="info">i</div>
  <div class="pair" style="margin-top:28px">
    <div><div class="val">17 Aug</div><div class="cap">Period Start</div></div>
    <div><div class="val">30 Aug</div><div class="cap">Period End</div></div>
  </div>
  <div style="display:flex;padding:10px 12px 0 24px;gap:10px">
    <div style="width:110px">
      <div class="val">01:00 29-Aug</div><div class="cap">Start Next Night Rest Before</div>
      <div style="margin-top:8px" class="val">1</div><div class="cap">Consecutive Night Rests Required</div>
    </div>
    <div class="days" style="width:150px">
      <span class="day">12</span><span class="day">13</span><span class="day miss">14</span><span class="day miss">15</span><span class="day">16</span><span class="day miss">17</span>
      <span class="day miss">18</span><span class="day miss">19</span><span class="day miss">20</span><span class="day miss">21</span><span class="day">22</span><span class="day miss">23</span>
      <span class="day">24</span><span class="day now">25</span>
    </div>
  </div>
  <div class="dot" style="left:7px;top:70px"></div>
</div>

<!-- phone screen -->
<div class="screen">
  <div class="status"><span>8:49 ➤</span><span style="font-size:10px">▮▮▮ ◠ ▭</span></div>
  <div class="head">
    <div style="display:flex;gap:14px;align-items:center">
      <span style="font-size:16px">≡</span>
      <div><div class="name">Jack Taylor</div><div class="lic">License : 1234567890</div></div>
    </div>
    <div style="text-align:right"><div style="color:#3cae5a;font-size:12px;margin-bottom:6px">✓</div><span class="sync">Sync Now</span></div>
  </div>
  <div class="option">
    <div style="font-size:10px">Dashboard Work Option <span style="color:var(--blue)">ⓘ</span></div>
    <div class="select"><span>BFM Solo</span><span style="color:var(--blue)">⌄</span></div>
  </div>
  <div class="card" style="height:66px">
    <div class="tab">Reset Rest Break</div><div class="info">i</div>
    <div class="pager" style="padding:40px 8px 0;font-size:10.5px"><span>Last reset restbreak ended</span><span>01:17 14-Aug</span></div>
  </div>
  <div class="card" style="padding-bottom:10px">
    <div class="tab">24 hr Rule</div><div class="info">i</div>
    <div class="pair" style="padding-top:30px;padding-bottom:8px;border-bottom:1px solid var(--line)">
      <div><div class="val">02:46 25-Aug</div><div class="cap">Period Start</div></div>
      <div><div class="val">02:46 26-Aug</div><div class="cap">Period End</div></div>
    </div>
    <div style="padding:12px 8px 0">
      <div class="cap" style="margin-bottom:4px">Work Completed</div>
      <div class="bar"><i style="width:50%"></i></div>
      <div class="pager cap" style="margin-top:4px"><span>0 hr</span><span>14 hr</span></div>
      <div class="grid" style="margin-top:10px">
        <div><div class="val">07:03</div><div class="cap">Work Completed</div></div>
        <div><div class="val">01:00</div><div class="cap">Maximum Continuous Rest</div></div>
        <div><div class="val">06:57</div><div class="cap">Work Remaining</div></div>
        <div><div class="val">19:46 25-Aug</div><div class="cap">Start 7 hr Rest Before</div><span class="cell-dot"></span></div>
        <div><div class="val">15:57</div><div class="cap">Period Remaining</div></div>
        <div><div class="val">0 / 1</div><div class="cap">7 hr Rests Found/Required</div></div>
      </div>
      <div class="pager" style="margin-top:10px"><span class="btn">‹ Previous</span><span><span class="val">1/1</span><br><span class="cap">Active Periods</span></span><span class="btn">Next ›</span></div>
    </div>
  </div>
  <div class="card" style="height:70px">
    <div class="tab">14 day Rule</div><div class="info">i</div>
    <div class="pair" style="padding-top:30px">
      <div><div class="val">01:17 14-Aug</div><div class="cap">Period Start</div></div>
      <div><div class="val">01:17 28-Aug</div><div class="cap">Period End</div></div>
    </div>
  </div>
  <div class="nav">
    <div><b>⏻</b>Logout</div><div><b>☰</b>Compliance</div><div><b>✉</b>Report transfer</div><div><b>⇥</b>Return to Shift</div>
  </div>
</div>

<!-- callouts -->
<div class="callout" style="left:545px;top:25px"><span class="time">01:17 27-Aug</span><span class="label">Start 24 hr Rest Before</span></div>
<div class="callout" style="left:813px;top:225px"><span class="time">19:46 25-Aug</span><span class="label">Start 7 hr Rest Before</span></div>
<div class="callout tall" style="left:97px;top:813px"><span class="time">01:00 29-Aug</span><span class="label">Start Next<br>Night Rest Before</span></div>

</div>
</body>
</html>
```